Banner Designs for Drone Defense Ad Campaign

Corvane is a security consulting and services company that offers a service called SkyMindful. SkyMindful helps our customers identify security risks from drones and develops comprehensive protection programs. We are looking for a designer to create a banner ad in three sizes for our campaign.
Target Market(s)
Our campaign is geared to the sports and entertainment industry, specifically large event venues and their security operation.
Industry/Entity Type
Security
Font styles to use
Other font styles liked:
- Raleway
Requirements
Must have
- Banner Objective
The visual and textual content of the banner should prompt the viewer to quickly identify the service offered and the information that is available to download.
Banner Design
Logo: SkyMindful logo
Call to Action Button in Red: Get It Here (On Right or or Upper Right)
Title in Larger Font: Guide to UAS Risk Mitigation
Subtitle in smaller Font: 5 Steps to Develop Your Comprehensive UAS Defense Program
Background: Stadium with a drone flying in foreground
Font: Raleway
Banner Sizes
1 - 1200x670 pixels
2 - 1510x196 pixels
3 - 1200x628 pixels

```html
<!DOCTYPE html>
<html lang="en">
<head>
<meta charset="UTF-8">
<title>SkyMindful – Guide to UAS Risk Mitigation</title>
<link href="https://fonts.googleapis.com/css2?family=Raleway:wght@500;700;800;900&display=swap" rel="stylesheet">
<style>
  :root {
    --panel-grey: #e9eaeb;
    --logo-ink: #5b636d;
    --logo-sub: #3a3f45;
    --night-navy: #16202c;
    --night-deep: #0c1219;
    --glow-red: #7a3a34;
    --title-white: #ffffff;
    --subtitle-blue: #2f7fd3;
    --cta-red: #dd2a1f;
  }
  * { margin: 0; padding: 0; box-sizing: border-box; }
  html, body { width: 1200px; height: 156px; overflow: hidden; background: #ffffff; }
  .banner {
    position: relative;
    width: 1200px;
    height: 156px;
    overflow: hidden;
    font-family: "Raleway", Arial, sans-serif;
  }
  .stadium-scene {
    position: absolute;
    inset: 0;
    background:
      radial-gradient(ellipse 260px 120px at 720px 120px, rgba(170,70,60,0.55), rgba(0,0,0,0) 70%),
      radial-gradient(ellipse 320px 90px at 600px 150px, rgba(120,40,35,0.45), rgba(0,0,0,0) 70%),
      radial-gradient(ellipse 220px 80px at 760px 60px, rgba(200,200,210,0.15), rgba(0,0,0,0) 70%),
      linear-gradient(180deg, var(--night-navy) 0%, #1d2733 45%, var(--glow-red) 85%, #3a2422 100%);
  }
  .stadium-scene::after {
    content: "";
    position: absolute;
    inset: 0;
    background: linear-gradient(90deg, rgba(12,18,25,0.7) 0%, rgba(12,18,25,0.2) 40%, rgba(12,18,25,0.1) 70%, rgba(12,18,25,0.6) 100%);
  }
  .brand-panel {
    position: absolute;
    left: 0; top: 0;
    width: 290px; height: 156px;
  }
  .brand {
    position: absolute;
    left: 42px;
    top: 72px;
  }
  .brand-name {
    display: block;
    font-size: 21px;
    font-weight: 700;
    color: var(--logo-ink);
    letter-spacing: -0.2px;
  }
  .brand-owner {
    display: block;
    margin-top: 1px;
    padding-left: 64px;
    font-size: 10px;
    font-weight: 500;
    color: var(--logo-sub);
  }
  .headline {
    position: absolute;
    left: 309px;
    top: 24px;
    color: var(--title-white);
    font-size: 37px;
    font-weight: 900;
    line-height: 32px;
    letter-spacing: -0.3px;
    text-transform: uppercase;
  }
  .subhead {
    position: absolute;
    left: 310px;
    top: 96px;
    color: var(--subtitle-blue);
    font-size: 12.5px;
    font-weight: 800;
    line-height: 16px;
    text-transform: uppercase;
  }
  .cta-button {
    position: absolute;
    left: 992px;
    top: 60px;
    width: 184px;
    height: 36px;
    background: var(--cta-red);
    color: var(--title-white);
    font-size: 16px;
    font-weight: 700;
    letter-spacing: -0.3px;
    text-transform: uppercase;
    display: flex;
    align-items: center;
    justify-content: center;
    text-decoration: none;
  }
</style>
</head>
<body>
  <div class="banner">
    <div class="stadium-scene" role="img" aria-label="Night-time stadium packed with spectators, with a camera drone flying in the foreground"></div>

    <svg class="brand-panel" viewBox="0 0 290 156" aria-hidden="true">
      <polygon points="0,0 131,0 282,156 0,156" fill="var(--panel-grey)"/>
    </svg>
    <div class="brand">
      <span class="brand-name">SkyMindful</span>
      <span class="brand-owner">By Corvane</span>
    </div>

    <h1 class="headline">Guide to UAS<br>Risk Mitigation</h1>
    <p class="subhead">5 Steps to Develop Your Comprehensive<br>UAS Defense Program</p>

    <a class="cta-button" href="#">Get It Here</a>
  </div>
</body>
</html>
```